Ashford Church of Grace (this will be used for new church sign) sign will be 4'x8' and would like also listed Sunday School 9:00am Worship Service 10:30am.

Logo Text

ASHFORD CHURCH OF GRACE

```html
<!DOCTYPE html>
<html lang="en">
<head>
<meta charset="utf-8">
<title>Ashford Church of Grace – Sign</title>
<link rel="stylesheet" href="https://fonts.googleapis.com/css2?family=Poppins:wght@600;700;800&display=swap">
<style>
  :root {
    --crimson: #b91d42;
    --gold: #c9a800;
    --gold-text: #ecd24a;
    --olive: #9b8412;
    --ink: #15152a;
    --white: #ffffff;
    --page: #ffffff;
  }
  * { margin: 0; padding: 0; box-sizing: border-box; }
  html, body { width: 1200px; height: 3143px; overflow: hidden; background: var(--page); }
  body { font-family: "Poppins", sans-serif; position: relative; }

  .sign {
    position: absolute;
    left: 50px; top: 471px;
    width: 1100px; height: 2200px;
    background: var(--white);
    overflow: hidden;
    box-shadow: 0 6px 18px rgba(0,0,0,0.25);
  }
  .sign-shapes { position: absolute; inset: 0; width: 1100px; height: 2200px; }

  .logo {
    position: absolute;
    left: 0; right: 0; top: 245px;
    display: flex; align-items: center; justify-content: center; gap: 22px;
  }
  .logo-dot { width: 46px; height: 46px; border-radius: 50%; background: var(--gold); }
  .logo-name { font-weight: 700; font-size: 62px; color: var(--crimson); letter-spacing: -0.5px; }

  .title {
    position: absolute; left: 0; right: 0; top: 735px;
    text-align: center; font-weight: 700; line-height: 146px; font-size: 150px;
  }
  .title-first { color: var(--white); }
  .title-rest { color: var(--gold-text); }
  .title-rest.long { font-size: 138px; }

  .schedule {
    position: absolute; left: 0; right: 0; top: 1440px;
    text-align: center; font-weight: 700;
  }
  .schedule-day { color: var(--crimson); font-size: 150px; line-height: 160px; }
  .schedule-line { font-size: 104px; line-height: 124px; }
  .schedule-school, .schedule-time { color: var(--ink); }
  .schedule-worship { color: var(--olive); font-size: 100px; }

  .footer {
    position: absolute; left: 0; right: 0; top: 2000px; height: 200px;
    display: flex; align-items: center; justify-content: center;
    font-weight: 700; font-size: 54px; color: var(--ink);
  }
</style>
</head>
<body>
  <main class="sign">
    <svg class="sign-shapes" viewBox="0 0 1100 2200" aria-hidden="true">
      <rect class="band-crimson" x="0" y="300" width="1100" height="1400" fill="var(--crimson)"/>
      <path class="curve-gold-top" d="M0 0 H1100 V452 Q560 880 0 345 Z" fill="var(--gold)"/>
      <path class="curve-white-top" d="M0 0 H1100 V420 Q560 820 0 320 Z" fill="var(--white)"/>
      <path class="line-white-top" d="M0 462 Q560 890 1100 540" fill="none" stroke="var(--white)" stroke-width="6"/>
      <path class="line-white-bottom" d="M0 1441 Q550 977 1100 1451" fill="none" stroke="var(--white)" stroke-width="6"/>
      <path class="curve-gold-bottom" d="M0 1500 Q550 1010 1100 1587 V2200 H0 Z" fill="var(--gold)"/>
      <path class="curve-white-bottom" d="M0 1535 Q550 1065 1100 1640 V2200 H0 Z" fill="var(--white)"/>
    </svg>

    <div class="logo">
      <span class="logo-dot"></span>
      <span class="logo-name">Ashford Church of Grace</span>
    </div>

    <h1 class="title">
      <span class="title-first">ASHFORD</span><br>
      <span class="title-rest long">CHURCH OF</span><br>
      <span class="title-rest">GRACE</span>
    </h1>

    <section class="schedule">
      <p class="schedule-day">SUNDAY</p>
      <p class="schedule-line schedule-school">SCHOOL 9:00AM</p>
      <p class="schedule-line schedule-worship">WORSHIP SERVICE</p>
      <p class="schedule-line schedule-time">10:30AM</p>
    </section>

    <footer class="footer">www.ashfordchurchofgrace.com</footer>
  </main>
</body>
</html>
```